Letter and Envelope Design For Juniper Crest Realty

Please design a letter and an envelope incorporating our logo (See Attached). We are also launched a business card contest. Since we want them to match, please feel free to submit a design for both the business card and also the letter design and envelope.

Requirements
Must have
• The envelope, the letter and the business cards must match somehow connecting the designs. We want them to have something that holds them together besides the logo.

```html
<!DOCTYPE html>
<html lang="en">
<head>
<meta charset="utf-8">
<title>Juniper Crest Realty Stationery</title>
<link href="https://fonts.googleapis.com/css2?family=Montserrat:ital,wght@0,400;0,500;0,600;1,400&display=swap" rel="stylesheet">
<style>
  :root {
    --navy: #2d3278;
    --ink: #4a4a4a;
    --paper: #ffffff;
    --backdrop: #e4e6e8;
  }
  * { margin: 0; padding: 0; box-sizing: border-box; }
  html, body { width: 1154px; height: 1200px; overflow: hidden; }
  body {
    position: relative;
    background: var(--backdrop);
    font-family: "Montserrat", sans-serif;
    color: var(--ink);
  }
  .sheet {
    position: absolute;
    background: var(--paper);
    box-shadow: 0 2px 6px rgba(0,0,0,0.18);
    overflow: hidden;
  }
  .fill { position: absolute; background: var(--navy); }

  /* brand lockup */
  .brand { position: absolute; text-align: center; transform: translateX(-50%); white-space: nowrap; }
  .brand-circle { border: 2px solid var(--navy); border-radius: 50%; margin: 0 auto; }
  .brand-name { color: var(--navy); font-weight: 600; text-transform: uppercase; line-height: 1.1; }

  /* letterhead */
  .letterhead { left: 32px; top: 34px; width: 568px; height: 736px; }
  .letterhead .brand { left: 486px; top: 11px; }
  .letterhead .brand-circle { width: 54px; height: 54px; margin-bottom: 7px; }
  .letterhead .brand-name { font-size: 14px; letter-spacing: 1.5px; }
  .letterhead .brand-name.sub { font-size: 11px; letter-spacing: 3px; }
  .footer-text { position: absolute; font-size: 9.5px; font-weight: 600; color: var(--ink); }

  /* business card back */
  .card-back { left: 636px; top: 34px; width: 244px; height: 427px; }
  .card-back .brand { left: 122px; top: 166px; }
  .card-back .brand-circle { width: 60px; height: 60px; margin-bottom: 6px; }
  .card-back .brand-name { font-size: 13px; letter-spacing: 1px; }
  .card-back .brand-name.sub { font-size: 11px; letter-spacing: 3px; }

  /* business card front */
  .card-front { left: 854px; top: 483px; width: 245px; height: 427px; }
  .card-front .brand { left: 180px; top: 17px; }
  .card-front .brand-circle { width: 36px; height: 36px; margin-bottom: 3px; border-width: 1.5px; }
  .card-front .brand-name { font-size: 9px; letter-spacing: 0.8px; }
  .card-front .brand-name.sub { font-size: 7px; letter-spacing: 2px; }
  .contact { position: absolute; left: 41px; font-size: 9px; color: var(--ink); }
  .contact-name { font-size: 14px; font-weight: 500; color: var(--navy); }
  .contact-role { font-size: 11px; font-style: italic; }

  /* envelope */
  .envelope { left: 38px; top: 806px; width: 796px; height: 344px; }
  .envelope .brand { left: 126px; top: 110px; }
  .envelope .brand-circle { width: 80px; height: 80px; margin-bottom: 8px; border-width: 3px; }
  .envelope .brand-name { font-size: 18px; letter-spacing: 1.5px; }
  .envelope .brand-name.sub { font-size: 16px; letter-spacing: 5px; }
  .envelope-return { position: absolute; right: 10px; top: 322px; font-size: 12px; font-weight: 600; }
</style>
</head>
<body>

  <section class="sheet letterhead">
    <div class="fill" style="left:0;top:0;width:54px;height:736px"></div>
    <div class="fill" style="left:58px;top:0;width:5px;height:736px"></div>
    <div class="brand">
      <div class="brand-circle"></div>
      <div class="brand-name">Juniper Crest</div>
      <div class="brand-name sub">Realty</div>
    </div>
    <div class="footer-text" style="left:82px;top:688px">(555) 214-7788</div>
    <div class="footer-text" style="left:82px;top:701px">www.junipercrestrealty.com</div>
    <div class="footer-text" style="right:24px;top:701px">48 Crestline Avenue • Fairhaven • State • 20418</div>
  </section>

  <section class="sheet card-back">
    <div class="fill" style="left:44px;top:0;width:157px;height:148px"></div>
    <div class="fill" style="left:44px;top:152px;width:157px;height:3px"></div>
    <div class="brand">
      <div class="brand-circle"></div>
      <div class="brand-name">Juniper Crest</div>
      <div class="brand-name sub">Realty</div>
    </div>
    <div class="fill" style="left:44px;top:273px;width:157px;height:3px"></div>
    <div class="fill" style="left:44px;top:280px;width:157px;height:147px"></div>
  </section>

  <section class="sheet card-front">
    <div class="fill" style="left:0;top:0;width:26px;height:427px"></div>
    <div class="fill" style="left:29px;top:0;width:4px;height:427px"></div>
    <div class="brand">
      <div class="brand-circle"></div>
      <div class="brand-name">Juniper Crest</div>
      <div class="brand-name sub">Realty</div>
    </div>
    <div class="contact contact-name" style="top:284px">Daniel Hayes</div>
    <div class="contact contact-role" style="top:306px">Realtor</div>
    <div class="contact" style="top:328px">48 Crestline Avenue</div>
    <div class="contact" style="top:341px">Fairhaven • State • 20418</div>
    <div class="contact" style="top:363px">(555) 214-7788</div>
    <div class="contact" style="top:380px">dhayes@junipercrestrealty.com</div>
    <div class="contact" style="top:400px">www.junipercrestrealty.com</div>
  </section>

  <section class="sheet envelope">
    <div class="fill" style="left:24px;top:0;width:204px;height:88px"></div>
    <div class="fill" style="left:24px;top:94px;width:204px;height:4px"></div>
    <div class="brand">
      <div class="brand-circle"></div>
      <div class="brand-name">Juniper Crest</div>
      <div class="brand-name sub">Realty</div>
    </div>
    <div class="fill" style="left:24px;top:247px;width:204px;height:4px"></div>
    <div class="fill" style="left:24px;top:254px;width:204px;height:90px"></div>
    <div class="envelope-return">48 Crestline Avenue • Fairhaven • State • 20418</div>
  </section>

</body>
</html>
```